International Company needs a Letterhead & Envelope Design

Our Company name is Brightfold Harbor Limited.
We'd like to ask the Designers for the luxurious and sophisticated design. Our logo is very simple and neat with letter logos, so we look forward to more professional and refined designs from Designers.
We look forward to providing you with a great design.
Thanks very much in advance.

```html
<!DOCTYPE html>
<html lang="en">
<head>
<meta charset="utf-8">
<title>Brightfold Harbor Limited – Stationery</title>
<link href="https://fonts.googleapis.com/css2?family=Lato:wght@400;700&family=Open+Sans:wght@400;600&display=swap" rel="stylesheet">
<style>
  :root{
    --ink:#0b0b0b;
    --swoosh:#5a5a5a;
    --brand:#6b6b6b;
    --paper:#ffffff;
    --text:#3c3c3c;
    --muted:#555;
    --backdrop:#c9c9c9;
  }
  *{margin:0;padding:0;box-sizing:border-box}
  html,body{width:1200px;height:1200px;overflow:hidden;background:var(--backdrop)}
  body{position:relative;font-family:"Open Sans",sans-serif;color:var(--text)}
  .sheet{position:absolute;background:var(--paper);box-shadow:0 3px 8px rgba(0,0,0,.25);overflow:hidden}
  .sheet svg.art{position:absolute;left:0;top:0;width:100%;height:100%}
  .brand-name{position:absolute;font-family:"Lato",sans-serif;font-weight:700;color:var(--brand);letter-spacing:.5px;white-space:nowrap}

  /* Letterhead */
  .letterhead{left:131px;top:331px;width:552px;height:711px}
  .letterhead .brand-name{left:52px;top:18px;font-size:20px}
  .contact-block{position:absolute;left:372px;top:28px;border-left:1px solid #999;padding-left:5px;font-family:"Lato",sans-serif;font-size:10.5px;line-height:13px;color:var(--muted)}
  .contact-block div{display:flex;align-items:center;gap:3px}
  .contact-block svg{width:7px;height:7px;fill:#222}
  .letter-body{position:absolute;left:52px;top:128px;width:446px;font-size:8.6px;line-height:16px}
  .letter-body p{margin-bottom:16px;text-align:justify}
  .letter-body .meta{line-height:11px;margin-bottom:22px}
  .signature{width:130px;height:16px;margin:6px 0 4px;background:linear-gradient(90deg,#e6e6e6,#f4f4f4)}
  .signer{font-size:10.5px;color:#222;line-height:14px}
  .footer-address{position:absolute;right:46px;bottom:22px;text-align:right;font-family:"Lato",sans-serif;font-size:10.5px;line-height:13px;color:#fff}

  /* Envelope front */
  .envelope-front{left:734px;top:599px;width:411px;height:205px}
  .envelope-front .brand-name{left:22px;top:14px;font-size:15px}
  .envelope-contact{position:absolute;left:22px;top:156px;width:362px;font-family:"Lato",sans-serif;font-size:7px;color:#222}
  .envelope-contact .rule{height:1px;background:#222;margin:5px 0 5px}
  .envelope-contact b{font-weight:700}

  /* Envelope back */
  .envelope-back{left:736px;top:840px;width:406px;height:202px}
  .envelope-back .brand-name{left:0;right:0;top:12px;text-align:center;font-size:15px}
</style>
</head>
<body>

<section class="sheet letterhead">
  <svg class="art" viewBox="0 0 690 889" preserveAspectRatio="none" aria-hidden="true">
    <path d="M0 0H690V34C600 6 480 10 380 30C250 56 120 82 0 72Z" fill="var(--ink)"/>
    <path d="M282 52C430 14 600 4 690 44V62C600 14 440 22 282 52Z" fill="var(--swoosh)"/>
    <path d="M0 792C60 830 250 858 420 822C250 842 80 842 0 818Z" fill="var(--swoosh)"/>
    <path d="M0 824C150 870 400 842 690 804V889H0Z" fill="var(--ink)"/>
  </svg>
  <div class="brand-name">Brightfold Harbor</div>
  <div class="contact-block">
    <div><svg viewBox="0 0 10 10"><path d="M1 3C1 1 2 1 3 1L4 3 3 4C4 6 5 7 6 7L7 6 9 7C9 8 9 9 7 9 4 9 1 6 1 3Z"/></svg>044-555 018 274</div>
    <div><svg viewBox="0 0 10 10"><path d="M0 2H10V8H0Z M0 2L5 6 10 2" fill="#222" stroke="#fff" stroke-width=".8"/></svg>hello@brightfoldharbor.com</div>
    <div><svg viewBox="0 0 10 10"><circle cx="5" cy="5" r="4.5"/></svg>www.brightfoldharbor.com</div>
  </div>

  <div class="letter-body">
    <p class="meta">Issuing Date: May 5, 2018</p>
    <p class="meta">Name Of Employee Mr. Halvorsen<br>Address of Employee<br>Address Line 2 etc..</p>
    <p>Dear Mr. Halvorsen</p>
    <p>Lorem Ipsum has been the industry's standard dummy text ever since the 1500s, when an unknown printer took a galley of type and scrambled it to make a type specimen book. It has survived not only five centuries, but also the leap into electronic typesetting, remaining essentially unchanged. It was popularised in the 1960s with the release of Letraset sheets containing Lorem Ipsum passages, and more recently with desktop publishing software like Aldus PageMaker including versions of Lorem Ipsum.</p>
    <p>Lorem Ipsum is simply dummy text of the printing and typesetting industry. Lorem Ipsum has been the industry's standard dummy text ever since the 1500s, when an unknown printer took a galley of type and scrambled it to make a type specimen book.</p>
    <p>It has survived not only five centuries, but also the leap into electronic typesetting, remaining essentially unchanged. It was popularised in the 1960s with the release of Letraset sheets containing Lorem Ipsum passages.</p>
    <p style="margin-bottom:0">Yours Sincerely</p>
    <div class="signature" role="img" aria-label="Handwritten signature of Elian Rourke"></div>
    <div class="signer">Elian Rourke</div>
    <div>Managing Director</div>
  </div>

  <div class="footer-address">421, Address line here<br>45452, Country Name</div>
</section>

<section class="sheet envelope-front">
  <svg class="art" viewBox="0 0 513 256" preserveAspectRatio="none" aria-hidden="true">
    <path d="M0 0H513V18C440 0 330 6 250 24C160 44 80 56 0 54Z" fill="var(--ink)"/>
    <path d="M205 38C320 8 450 0 513 22V38C450 6 330 16 205 38Z" fill="var(--swoosh)"/>
  </svg>
  <div class="brand-name">Brightfold Harbor</div>
  <div class="envelope-contact">
    <div><b>P:</b> 044-555 018 274 | <b>E:</b> hello@brightfoldharbor.com | www.brightfoldharbor.com</div>
    <div class="rule"></div>
    <div>421, Address line here 45452, Country Name</div>
  </div>
</section>

<section class="sheet envelope-back">
  <svg class="art" viewBox="0 0 508 253" preserveAspectRatio="none" aria-hidden="true">
    <path d="M0 0H508L490 59H20Z" fill="var(--ink)"/>
  </svg>
  <div class="brand-name">Brightfold Harbor</div>
</section>

</body>
</html>
```